The Duchess of Nestware is an online store specialising in all things for the home Bathroom, Kitchen,

I need a business card designed that is professional and elegant, yet not conservative. We will be wanting to brand the entire business and will have videos made where we will be interacting with the product, testing the products and basically creating an online interactive community for all those people interested in all things to do with the Home and the activities that take place in and around the home.

Target Market(s)

30-65yr old Men and Women who LOVE their Home and see it as their primary place of Happiness, their sanctuary!

Industry/Entity Type

Business

Contact Information for Business Card

www.duchessofnestware.example The Duchess Of Nestware-PO Box 58316, Marlow Flats, Auckland. NEW ZEALAND. info@duchessofnestware.example
Love your Home! Corinne Dale-Petrakou

Font styles to use
Decorative
Script

Colors
9bcb3b
33b8a4
85cae6
b7a5cd
eda3c7
e667a6
d2a4cc
fdf9cf
fee18a

Requirements
Must have
• Attractive colours. Must feel Elegant, yet simple. A font that is rounded without sharp edges. Organic feel to the card, something raw with texture.
Nice to have
• I like the logo deign that I gave in the photos, something feminine, but fun.
Should not have
• I dont like sharp edges, or linear design. I like organic, flowing, fractal type design. Something that looks beautiful in form when you look at it.

```html
<!DOCTYPE html>
<html lang="en">
<head>
<meta charset="utf-8">
<title>The Duchess of Nestware — Business Card</title>
<link href="https://fonts.googleapis.com/css2?family=Josefin+Sans:wght@300;400&family=Courgette&display=swap" rel="stylesheet">
<style>
  :root {
    --backdrop: #ece8e4;
    --paper: #ffffff;
    --paper-shade: #f7f5f6;
    --sky: #5aaed3;
    --pink: #e8348f;
    --ink: #2a2a2a;
  }
  * { margin: 0; padding: 0; box-sizing: border-box; }
  html, body {
    width: 1200px; height: 1200px; overflow: hidden;
    background: var(--backdrop);
  }
  .sheet {
    width: 1200px; height: 1200px;
    display: flex; flex-direction: column; align-items: center; justify-content: center;
    gap: 60px;
  }
  .card {
    position: relative;
    width: 900px; height: 514px;
    background: var(--paper);
    box-shadow: 0 10px 30px rgba(0,0,0,.15);
    overflow: hidden;
  }
  .card--front { background: linear-gradient(160deg, var(--paper), var(--paper-shade)); }

  .ornament { position: absolute; }
  .ornament--front-left { left: -40px; top: 60px; width: 380px; height: 470px; }
  .ornament--front-right { right: -60px; top: -40px; width: 220px; height: 230px; }
  .ornament--back-left { left: -60px; bottom: -60px; width: 300px; height: 300px; }
  .ornament--back-right { right: -60px; top: 110px; width: 220px; height: 260px; }

  .business-name {
    font-family: "Josefin Sans", sans-serif;
    font-weight: 400;
    color: var(--sky);
    letter-spacing: .04em;
    text-align: center;
    line-height: 1.2;
  }
  .front-brand {
    position: absolute; left: 350px; top: 215px; width: 460px;
  }
  .front-brand .business-name { font-size: 40px; }

  .back-content {
    position: absolute; left: 200px; top: 70px; width: 540px; text-align: center;
  }
  .holder-name {
    font-family: "Courgette", cursive;
    font-weight: 400;
    font-size: 46px;
    color: var(--sky);
  }
  .holder-name .surname { color: var(--pink); }
  .contact {
    list-style: none;
    margin-top: 22px;
    font-family: "Josefin Sans", sans-serif;
    font-size: 17px; letter-spacing: .06em;
    color: var(--ink);
    text-transform: uppercase;
    line-height: 1.6;
  }
  .back-brand { margin-top: 34px; }
  .back-brand .business-name { font-size: 28px; }
</style>
</head>
<body>
<main class="sheet">

  <section class="card card--front" aria-label="Business card front">
    <svg class="ornament ornament--front-left" viewBox="0 0 380 470" role="img" aria-label="Flowing mandala ornament fading from sky blue through violet to pink">
      <defs>
        <linearGradient id="fadeLeft" x1="0" y1="0" x2="1" y2="1">
          <stop offset="0" stop-color="#85cae6"/>
          <stop offset=".5" stop-color="#b07ad0"/>
          <stop offset="1" stop-color="#e8348f"/>
        </linearGradient>
      </defs>
      <path d="M0 60 Q120 0 200 80 Q300 140 380 240 Q280 280 270 370 Q180 470 0 470 Z" fill="url(#fadeLeft)" opacity=".85"/>
    </svg>
    <svg class="ornament ornament--front-right" viewBox="0 0 220 230" role="img" aria-label="Pink mandala ornament in the corner">
      <path d="M40 0 H220 V230 Q150 200 110 170 Q20 140 0 100 Q60 60 40 0 Z" fill="#e8348f" opacity=".8"/>
    </svg>

    <div class="front-brand">
      <p class="business-name">The Duchess of Nestware</p>
    </div>
  </section>

  <section class="card card--back" aria-label="Business card back">
    <svg class="ornament ornament--back-left" viewBox="0 0 300 300" role="img" aria-label="Mandala ornament fading from blue to pink">
      <defs>
        <linearGradient id="fadeBack" x1="0" y1="0" x2="1" y2="1">
          <stop offset="0" stop-color="#85cae6"/>
          <stop offset=".5" stop-color="#b07ad0"/>
          <stop offset="1" stop-color="#e8348f"/>
        </linearGradient>
      </defs>
      <path d="M0 40 Q110 20 180 70 Q270 100 300 160 Q230 190 220 250 Q160 300 0 300 Z" fill="url(#fadeBack)" opacity=".85"/>
    </svg>
    <svg class="ornament ornament--back-right" viewBox="0 0 220 260" role="img" aria-label="Pink and blue mandala ornament on the right edge">
      <defs>
        <linearGradient id="fadeRight" x1="0" y1="0" x2="0" y2="1">
          <stop offset="0" stop-color="#e8348f"/>
          <stop offset="1" stop-color="#85cae6"/>
        </linearGradient>
      </defs>
      <path d="M220 0 V260 Q130 240 80 190 Q0 150 20 120 Q90 90 110 40 Q160 10 220 0 Z" fill="url(#fadeRight)" opacity=".85"/>
    </svg>

    <div class="back-content">
      <h1 class="holder-name">Corinne Dale-<span class="surname">Petrakou</span></h1>
      <ul class="contact">
        <li>PO Box 58316</li>
        <li>Marlow Flats, Auckland, New Zealand</li>
        <li>info@duchessofnestware.example</li>
        <li>www.duchessofnestware.example</li>
      </ul>
      <div class="back-brand">
        <p class="business-name">The Duchess of Nestware</p>
      </div>
    </div>
  </section>

</main>
</body>
</html>
```